Professional Services - letterhead / business cards

The company (veltaro holdings) will provide services to Investment Funds and large investors in Spain. I have recently chosen a logo that I am attaching.

I would like a simple stationary design that i could use as letter head, business cards and "with compliments" cards.

I am not quite sure which color I will mostly use for the logo, in the email signature I will probably lean towards the white background and grey letters. I am attaching my favourite options.

Target Market(s)

Large Multinationals, Investment funds and Law firms

Industry/Entity Type

Business

Requirements
Must have
• my details are:
Luis R. Andrade
Veltaro Holdings S.L.
Casa de Valdehondo
Calle del Olmo Tardío 42
28017 Madrid
T: +34 (91) 807-3356
M: +34 (655) 718-904
e-mail: landrade@veltaroholdings.example

```html
<!DOCTYPE html>
<html lang="en">
<head>
<meta charset="utf-8">
<title>Veltaro Holdings – With Compliments Card</title>
<link rel="stylesheet" href="https://fonts.googleapis.com/css2?family=Questrial&display=swap">
<style>
  :root {
    --backdrop: #d9d9d9;
    --card: #f4f4f4;
    --ink: #25245c;
    --shadow: rgba(0, 0, 0, 0.18);
  }
  * { margin: 0; padding: 0; box-sizing: border-box; }
  html, body {
    width: 1200px;
    height: 720px;
    overflow: hidden;
    background: var(--backdrop);
  }
  body {
    display: flex;
    align-items: center;
    justify-content: center;
    font-family: "Questrial", sans-serif;
    color: var(--ink);
  }
  .compliments-card {
    position: relative;
    width: 1000px;
    height: 500px;
    background: var(--card);
    box-shadow: 0 6px 24px var(--shadow);
  }
  .brand-name {
    position: absolute;
    top: 92px;
    right: 90px;
    font-size: 40px;
    letter-spacing: 0.5px;
    line-height: 1;
    white-space: nowrap;
  }
  .greeting {
    position: absolute;
    left: 62px;
    top: 300px;
    font-size: 30px;
    line-height: 1;
  }
  .contact-block {
    position: absolute;
    left: 690px;
    top: 352px;
    padding-left: 18px;
    border-left: 1.5px solid var(--ink);
    font-size: 14px;
    line-height: 1.35;
    height: 122px;
  }
  .contact-lines {
    display: grid;
    grid-template-columns: 22px auto;
    margin-bottom: 10px;
  }
  .contact-label { font-size: 12px; padding-top: 1px; }
  .address { font-style: normal; }
</style>
</head>
<body>
  <main class="compliments-card">
    <div class="brand-name">veltaro holdings</div>

    <p class="greeting">With compliments</p>

    <section class="contact-block">
      <div class="contact-lines">
        <span class="contact-label">T</span><span>+34 (91) 807-3356</span>
        <span class="contact-label">M</span><span>+34 (655) 718-904</span>
        <span class="contact-label">E</span><span>landrade@veltaroholdings.example</span>
      </div>
      <address class="address">
        Casa de Valdehondo<br>
        Calle del Olmo Tardío 42,<br>
        28017 Madrid
      </address>
    </section>
  </main>
</body>
</html>
```